PowerPoint Template Design for Quarry Lending

Design a PowerPoint template for Quarry Lending, tailored for presentations to sophisticated mortgage servicing investors. The template should reflect a high level of professionalism, with a clean and modern aesthetic that resonates with an informed and discerning audience. The design must effectively integrate Quarry Lending's branding elements, ensuring a coherent visual narrative that reinforces our reputation for expertise and reliability in the mortgage servicing sector.

```html
<!DOCTYPE html>
<html lang="en">
<head>
<meta charset="utf-8">
<title>Quarry Lending – Presentation Template</title>
<link href="https://fonts.googleapis.com/css2?family=Montserrat:wght@600;800&family=Roboto:wght@400;500;700&display=swap" rel="stylesheet">
<style>
:root{
  --navy:#27264f;
  --teal:#3ab0ad;
  --orange:#f29a2e;
  --board:#c9cacd;
  --ink:#6b6b75;
  --white:#ffffff;
}
*{box-sizing:border-box;margin:0;padding:0}
html,body{width:902px;height:1200px;overflow:hidden;background:var(--board)}
.board{position:relative;width:902px;height:1200px;background:var(--board);font-family:'Roboto',sans-serif}
.slide{position:absolute;width:270px;height:152px;background:var(--white);overflow:hidden;box-shadow:0 1px 3px rgba(0,0,0,.18)}
.abs{position:absolute}
.ph{position:absolute}
.ph-sky{background:linear-gradient(160deg,#a9c7e6 0%,#4f79a8 55%,#1f3a5c 100%)}
.ph-house{background:linear-gradient(180deg,#b9cfe0 0%,#d9d6cf 45%,#7d8f6a 100%)}
.ph-city{background:linear-gradient(180deg,#b7c3cf 0%,#7e8c9b 60%,#4f5a66 100%)}
.ph-dark{background:linear-gradient(160deg,#5b6470 0%,#23272d 60%,#15171a 100%)}
.ph-modern{background:linear-gradient(180deg,#cfd9e2 0%,#8c8580 50%,#4f5b45 100%)}
.ph-people{background:linear-gradient(135deg,#c7d6e3 0%,#7f93a8 55%,#3d4f66 100%)}
.sq-teal{position:absolute;background:var(--teal)}
.sq-orange{position:absolute;background:var(--orange)}
.title{position:absolute;font-family:'Roboto',sans-serif;font-weight:700;color:var(--navy);line-height:1.1}
.tiny{position:absolute;font-size:3.2px;line-height:1.4;color:var(--ink)}
.tiny.white{color:#eef8f8}
.label{position:absolute;font-weight:700;color:var(--navy);font-size:5px}
.label.orange{color:var(--orange)}
.brand{position:absolute;font-family:'Roboto',sans-serif;font-weight:700;color:var(--navy);font-size:8px;display:flex;align-items:center;gap:3px}
.brand i{display:block;width:5px;height:5px;background:var(--orange)}
.url-strip{position:absolute;background:var(--teal);color:var(--white);font-size:4px;font-weight:500;display:flex;align-items:center;justify-content:center}
.url-strip span{transform:rotate(-90deg);white-space:nowrap}
.num-dot{position:absolute;width:11px;height:11px;border-radius:50%;background:var(--orange);color:#fff;font-size:6px;font-weight:700;display:flex;align-items:center;justify-content:center}
.icon-box{position:absolute;width:10px;height:10px;border-radius:2px;background:var(--orange)}
.card{position:absolute;border:1.5px solid var(--teal);border-radius:5px;background:#fff}
.bullets{position:absolute;list-style:none;font-size:5px;color:var(--ink)}
.bullets li{margin-bottom:6.5px;padding-left:9px;position:relative}
.bullets li::before{content:"";position:absolute;left:0;top:1.5px;width:2.5px;height:2.5px;background:var(--navy)}
.avatar{position:absolute;width:20px;height:20px;border-radius:50%;border:1.5px solid var(--orange);background:linear-gradient(180deg,#e6ded6,#b9aca0)}
.phone{position:absolute;border:1.5px solid var(--navy);border-radius:4px;background:#fff}
svg{position:absolute;overflow:visible}
</style>
</head>
<body>
<div class="board">

<!-- Row 1 -->
<section class="slide" style="left:34px;top:36px">
  <div class="ph ph-sky" role="img" aria-label="Glass office towers against a blue sky" style="left:75px;top:0;width:195px;height:152px"></div>
  <div class="brand" style="left:8px;top:14px"><i></i>Quarry Lending</div>
  <div class="abs" style="left:37px;top:53px;width:148px;height:38px;background:#fff"></div>
  <div class="url-strip" style="left:24px;top:53px;width:5px;height:44px"><span>quarrylending.com</span></div>
  <div class="abs" style="left:38px;top:59px;font-family:'Montserrat',sans-serif;font-weight:800;font-size:13px;color:var(--navy)">LIVE BETTER</div>
  <div class="abs" style="left:38px;top:76px;font-family:'Montserrat',sans-serif;font-weight:600;font-size:10px;color:var(--orange)">MORTGAGE <span style="color:var(--navy)">SMARTER</span></div>
  <div class="sq-orange" style="left:8px;top:138px;width:7px;height:7px"></div>
</section>

<section class="slide" style="left:317px;top:36px">
  <div class="sq-teal" style="left:0;top:0;width:69px;height:68px"></div>
  <div class="ph ph-modern" role="img" aria-label="Modern two-storey house with garden" style="left:19px;top:28px;width:75px;height:108px"></div>
  <div class="sq-orange" style="left:94px;top:47px;width:13px;height:8px"></div>
  <div class="title" style="right:18px;top:12px;font-size:9px;font-weight:500">Agenda</div>
  <div class="sq-orange" style="left:255px;top:14px;width:15px;height:7px"></div>
  <div class="label" style="left:125px;top:48px"><span style="color:var(--orange)">1.</span> Lorem ipsum</div>
  <div class="tiny" style="left:132px;top:55px;width:100px">Lorem ipsum dolor sit amet, consectetuer adipiscing elit, sed diam nonummy nibh euismod tincid</div>
  <div class="label" style="left:125px;top:72px"><span style="color:var(--orange)">2.</span> Lorem ipsum</div>
  <div class="tiny" style="left:132px;top:79px;width:100px">Lorem ipsum dolor sit amet, consectetuer adipiscing elit, sed diam nonummy nibh euismod tincid</div>
  <div class="label" style="left:125px;top:96px"><span style="color:var(--orange)">3.</span> Lorem ipsum</div>
  <div class="tiny" style="left:132px;top:103px;width:100px">Lorem ipsum dolor sit amet, consectetuer adipiscing elit, sed diam nonummy nibh euismod tincid</div>
  <div class="label" style="left:125px;top:120px"><span style="color:var(--orange)">4.</span> Lorem ipsum</div>
  <div class="tiny" style="left:132px;top:127px;width:100px">Lorem ipsum dolor sit amet, consectetuer adipiscing elit, sed diam nonummy nibh euismod tincid</div>
</section>

<section class="slide" style="left:598px;top:36px">
  <div class="sq-teal" style="left:16px;top:18px;width:9px;height:9px"></div>
  <div class="title" style="left:20px;top:34px;font-size:16px">Creative<br>Heading</div>
  <div class="ph ph-house" role="img" aria-label="White farmhouse with trees" style="left:105px;top:17px;width:165px;height:64px"></div>
  <div class="tiny" style="left:105px;top:90px;width:130px">Lorem ipsum dolor sit amet, consectetuer adipiscing elit, sed diam nonummy nibh euismod tincidunt erat volutpat.<br><br>Ut wisi enim ad minim veniam, quis nostrud exerci tation ullamcorper suscipit lobortis nisl ut aliquip ex ea commodo consequat.</div>
  <div class="sq-orange" style="left:105px;top:132px;width:9px;height:20px"></div>
</section>

<!-- Row 2 -->
<section class="slide" style="left:34px;top:200px">
  <div class="sq-teal" style="left:18px;top:34px;width:10px;height:10px"></div>
  <div class="title" style="left:18px;top:50px;font-size:11px;font-weight:500">Lorem Ipsum<br>Dolor Sit<br>Ametkeeper.</div>
  <div class="ph ph-house" role="img" aria-label="Modern gabled house at dusk" style="left:100px;top:30px;width:68px;height:43px"></div>
  <div class="ph ph-city" role="img" aria-label="City skyline" style="left:182px;top:30px;width:68px;height:43px"></div>
  <div class="sq-orange" style="left:253px;top:66px;width:17px;height:7px"></div>
  <div class="label orange" style="left:100px;top:81px">Dolor Sit</div>
  <div class="tiny" style="left:100px;top:88px;width:70px">Lorem ipsum dolor sit amet, consectetuer adipiscing elit, sed diam nonummy nibh euismod tincidunt ut laoreet dolore magna<br><br>aliquam erat volutpat. Ut wisi enim ad minim veniam, quis nostrud exerci tation ullamcorper suscipit lobortis nisl ut aliquip</div>
  <div class="label orange" style="left:182px;top:81px">Laoreet Dolore</div>
  <div class="tiny" style="left:182px;top:88px;width:70px">Lorem ipsum dolor sit amet, consectetuer adipiscing elit, sed diam nonummy nibh euismod tincidunt ut<br><br>laoreet dolore magna aliquam erat volutpat. Ut wisi enim ad minim veniam, quis nostrud exerci tation suscipit lobortis nisl ut aliquip ex ea</div>
</section>

<section class="slide" style="left:317px;top:200px">
  <div class="ph ph-dark" role="img" aria-label="Dark glass skyscraper seen from below" style="left:115px;top:0;width:155px;height:152px"></div>
  <div class="sq-orange" style="left:250px;top:13px;width:11px;height:11px"></div>
  <div class="sq-teal" style="left:30px;top:52px;width:50px;height:40px;clip-path:polygon(0 0,100% 0,100% 100%,45% 100%)"></div>
  <div class="abs" style="left:37px;top:50px;font-family:'Montserrat',sans-serif;font-weight:800;font-size:36px;color:var(--navy);letter-spacing:-2px">01</div>
  <div class="abs" style="left:88px;top:52px;width:102px;height:49px;background:#fff"></div>
  <div class="label orange" style="left:91px;top:59px;font-size:8px;font-weight:500">Part one</div>
  <div class="tiny" style="left:91px;top:70px;width:92px">Lorem ipsum dolor sit amet, consectetuer adipiscing elit, sed diam nonummy nibh<br><br>laoreet dolore magna aliquam erat volutpat. Ut wisi enim ad minim veniam, quis nostrud exerci tation</div>
  <div class="sq-orange" style="left:8px;top:137px;width:7px;height:7px"></div>
</section>

<section class="slide" style="left:598px;top:200px">
  <div class="sq-teal" style="left:0;top:18px;width:117px;height:134px"></div>
  <div class="abs" style="left:92px;top:22px;width:8px;height:8px;background:#fff"></div>
  <div class="title" style="left:18px;top:36px;font-size:11px;font-weight:500;color:var(--navy)">Lorem Ipsum<br>Dolor Sit<br>Ametkeeper.</div>
  <div class="tiny white" style="left:18px;top:94px;width:80px">Lorem ipsum dolor sit amet, consectetuer adipiscing elit, sed diam nonummy nibh euismod tincidunt erat volutpat.<br><br>Ut wisi enim ad minim veniam, quis nostrud exerci tation ullamcorper suscipit lobortis nisl ut aliquip ex ea commodo consequat.</div>
  <div class="sq-teal" style="left:259px;top:5px;width:7px;height:7px"></div>
  <div class="icon-box" style="left:124px;top:31px"></div>
  <div class="label" style="left:145px;top:32px;font-size:4.5px">Servicing Transfer</div>
  <div class="tiny" style="left:145px;top:38px;width:80px">Ipsum dolor sit amet, cons ectetuer adipiscing elit, sed diam nonummy nibh euismod tincidunt</div>
  <div class="icon-box" style="left:124px;top:58px"></div>
  <div class="label" style="left:145px;top:59px;font-size:4.5px">Purchasing</div>
  <div class="tiny" style="left:145px;top:65px;width:80px">Ipsum dolor sit amet, cons ectetuer adipiscing elit, sed diam nonummy nibh euismod tincidunt ut laoreet aliquam</div>
  <div class="icon-box" style="left:124px;top:88px"></div>
  <div class="label" style="left:145px;top:89px;font-size:4.5px">Refinancing</div>
  <div class="tiny" style="left:145px;top:95px;width:80px">Ipsum dolor sit amet, cons ectetuer adipiscing elit, sed diam nonummy nibh euismod</div>
  <div class="icon-box" style="left:124px;top:117px"></div>
  <div class="label" style="left:145px;top:118px;font-size:4.5px">Mortgage Calculator</div>
  <div class="tiny" style="left:145px;top:124px;width:80px">Ipsum dolor sit amet, cons ectetuer adipiscing elit, sed diam nonummy nibh euismod tincidunt</div>
</section>

<!-- Row 3 -->
<section class="slide" style="left:34px;top:364px">
  <div class="sq-teal" style="left:15px;top:15px;width:11px;height:11px"></div>
  <div class="title" style="left:15px;top:33px;font-size:11px;font-weight:500">Company<br><span style="font-size:16px;font-weight:700">Overview</span></div>
  <svg style="left:125px;top:13px" width="140" height="72" viewBox="0 0 140 72">
    <g font-size="4" fill="#666" text-anchor="end">
      <text x="6" y="4">60</text><text x="6" y="14">50</text><text x="6" y="24">40</text><text x="6" y="34">30</text><text x="6" y="44">20</text><text x="6" y="54">10</text><text x="6" y="64">0</text>
    </g>
    <g stroke="#ddd" stroke-width=".4">
      <line x1="9" y1="3" x2="137" y2="3"/><line x1="9" y1="13" x2="137" y2="13"/><line x1="9" y1="23" x2="137" y2="23"/><line x1="9" y1="33" x2="137" y2="33"/><line x1="9" y1="43" x2="137" y2="43"/><line x1="9" y1="53" x2="137" y2="53"/><line x1="9" y1="63" x2="137" y2="63"/>
    </g>
    <rect x="21" y="23" width="4" height="40" fill="var(--orange)"/><rect x="26" y="13" width="4" height="50" fill="var(--navy)"/>
    <rect x="46" y="52" width="4" height="11" fill="var(--navy)"/><rect x="51" y="28" width="4" height="35" fill="var(--orange)"/>
    <rect x="73" y="6" width="4" height="57" fill="var(--navy)"/><rect x="78" y="50" width="4" height="13" fill="var(--orange)"/>
    <rect x="100" y="11" width="4" height="52" fill="var(--orange)"/><rect x="105" y="33" width="4" height="30" fill="var(--navy)"/>
    <g font-size="4.5" fill="#444" text-anchor="middle"><text x="26" y="70">JAN</text><text x="51" y="70">FEB</text><text x="78" y="70">MAR</text><text x="105" y="70">APR</text></g>
  </svg>
  <svg style="left:8px;top:87px" width="115" height="48" viewBox="0 0 115 48">
    <g font-size="3" fill="#666" text-anchor="end"><text x="6" y="3">60</text><text x="6" y="10">50</text><text x="6" y="17">40</text><text x="6" y="24">30</text><text x="6" y="31">20</text><text x="6" y="38">10</text><text x="6" y="45">0</text></g>
    <g stroke="#e2e2e2" stroke-width=".3"><line x1="8" y1="2" x2="113" y2="2"/><line x1="8" y1="44" x2="113" y2="44"/></g>
    <polyline fill="none" stroke="var(--navy)" stroke-width=".6" points="14,36 25,40 37,27 48,8 60,15 72,27 84,22 96,14 107,32"/>
    <polyline fill="none" stroke="var(--orange)" stroke-width=".6" points="14,42 25,34 37,22 48,34 60,18 72,25 84,27 96,22 107,14"/>
    <g fill="var(--navy)"><circle cx="14" cy="36" r="1"/><circle cx="37" cy="27" r="1"/><circle cx="48" cy="8" r="1"/><circle cx="72" cy="27" r="1"/><circle cx="96" cy="14" r="1"/></g>
    <g font-size="2.5" fill="#666" text-anchor="middle"><text x="14" y="48">TEXT 01</text><text x="37" y="48">TEXT 03</text><text x="60" y="48">TEXT 05</text><text x="84" y="48">TEXT 07</text><text x="107" y="48">TEXT 09</text></g>
  </svg>
  <div class="label" style="left:140px;top:94px;font-size:4px">● Lorem ipsum</div>
  <div class="tiny" style="left:148px;top:99px;width:40px">Lorem ipsum dolor sit amet, consectetuer adipiscing elit</div>
  <div class="label orange" style="left:208px;top:94px;font-size:4px">● Lorem ipsum</div>
  <div class="tiny" style="left:216px;top:99px;width:40px">Lorem ipsum dolor sit amet, consectetuer adipiscing elit</div>
  <div class="label orange" style="left:140px;top:114px;font-size:4px">● Lorem ipsum</div>
  <div class="tiny" style="left:148px;top:119px;width:40px">Lorem ipsum dolor sit amet, consectetuer adipiscing elit</div>
  <div class="label" style="left:208px;top:114px;font-size:4px">● Lorem ipsum</div>
  <div class="tiny" style="left:216px;top:119px;width:40px">Lorem ipsum dolor sit amet, consectetuer adipiscing elit</div>
</section>

<section class="slide" style="left:317px;top:364px">
  <div class="sq-teal" style="left:0;top:9px;width:16px;height:11px"></div>
  <div class="title" style="left:20px;top:9px;font-size:10px;font-weight:500">Our Company Education</div>
  <div class="sq-orange" style="left:256px;top:6px;width:8px;height:8px"></div>
  <div class="card" style="left:55px;top:39px;width:45px;height:69px"></div>
  <div class="card" style="left:118px;top:39px;width:45px;height:69px"></div>
  <div class="card" style="left:181px;top:39px;width:45px;height:69px"></div>
  <svg style="left:95px;top:55px" width="95" height="45" viewBox="0 0 95 45"><g fill="none" stroke="var(--teal)" stroke-width="1.5"><path d="M5 0 L-10 40"/><path d="M68 0 L53 40"/></g><g fill="var(--teal)"><circle cx="4" cy="2" r="2"/><circle cx="-9" cy="38" r="2"/><circle cx="67" cy="2" r="2"/><circle cx="54" cy="38" r="2"/></g></svg>
  <div class="label" style="left:55px;top:65px;width:45px;text-align:center;font-size:4.5px">IDEA</div>
  <div class="tiny" style="left:59px;top:72px;width:37px;text-align:center">Lorem ipsum dolor sit amet, consectetuer adipiscing elit, sed diam nonummy nibh euismod tincidunt ut laoreet dolore magna</div>
  <div class="label" style="left:118px;top:65px;width:45px;text-align:center;font-size:4.5px">PROMOTION</div>
  <div class="tiny" style="left:122px;top:72px;width:37px;text-align:center">Lorem ipsum dolor sit amet, consectetuer adipiscing elit, sed diam nonummy nibh euismod tincidunt ut laoreet dolore magna</div>
  <div class="label" style="left:181px;top:65px;width:45px;text-align:center;font-size:4.5px">GROWTH</div>
  <div class="tiny" style="left:185px;top:72px;width:37px;text-align:center">Lorem ipsum dolor sit amet, consectetuer adipiscing elit, sed diam nonummy nibh euismod tincidunt ut laoreet dolore magna</div>
  <div class="tiny" style="left:35px;top:120px;width:200px;text-align:center">Lorem ipsum dolor sit amet, consectetuer adipiscing elit, sed diam nonummy nibh euismod tincidunt ut laoreet dolore magna aliquam erat volutpat. Ut wisi enim ad minim veniam, quis nostrud exerci tation ullamcorper suscipit lobortis nisl ut aliquip ex ea commodo consequat.</div>
</section>

<section class="slide" style="left:598px;top:364px">
  <div class="sq-teal" style="left:0;top:9px;width:16px;height:11px"></div>
  <div class="title" style="left:20px;top:9px;font-size:15px;font-weight:500">Our<br>Company</div>
  <div class="sq-orange" style="left:259px;top:6px;width:7px;height:7px"></div>
  <div class="tiny" style="left:20px;top:52px;width:80px">Lorem ipsum dolor sit amet, consectetuer adipiscing elit, sed diam nonummy nibh euismod tincidunt ut laoreet dolore magna aliquam erat volutpat. Ut wisi enim ad minim veniam, quis nostrud exerci tation ullamcorper suscipit lobortis nisl ut aliquip ex ea commodo consequat. Duis autem vel eum iriure dolor in hendrerit<br><br>Lorem ipsum dolor sit amet, consectetuer adipiscing elit, sed diam nonummy nibh. Lorem ipsum dolor sit amet, consectetuer adipiscing elit, sed diam nonummy nibh euismod tincidunt ut laoreet dolore magna aliquam erat volutpat.</div>
  <div class="abs" style="left:118px;top:21px;font-size:4.5px;font-weight:500;color:var(--navy)">CONSECTETUER ADIPISCING</div>
  <svg style="left:112px;top:31px" width="148" height="68" viewBox="0 0 148 68">
    <g font-size="4.5" fill="#666" text-anchor="end"><text x="7" y="4">60</text><text x="7" y="14">50</text><text x="7" y="24">40</text><text x="7" y="34">30</text><text x="7" y="44">20</text><text x="7" y="54">10</text><text x="7" y="64">0</text></g>
    <g stroke="#ddd" stroke-width=".4"><line x1="10" y1="3" x2="146" y2="3"/><line x1="10" y1="13" x2="146" y2="13"/><line x1="10" y1="23" x2="146" y2="23"/><line x1="10" y1="33" x2="146" y2="33"/><line x1="10" y1="43" x2="146" y2="43"/><line x1="10" y1="53" x2="146" y2="53"/><line x1="10" y1="63" x2="146" y2="63"/></g>
    <rect x="22" y="8" width="14" height="55" fill="var(--navy)"/><rect x="50" y="31" width="14" height="32" fill="var(--orange)"/>
    <rect x="78" y="16" width="14" height="47" fill="var(--navy)"/><rect x="106" y="35" width="14" height="28" fill="var(--orange)"/>
  </svg>
  <g></g>
  <div class="abs" style="left:126px;top:101px;font-size:4.5px;color:#444;width:130px;display:flex;justify-content:space-between;padding-right:10px"><span>JAN</span><span>FEB</span><span>MAR</span><span>APR</span></div>
  <div class="label orange" style="left:115px;top:113px;font-size:4.5px"><span style="color:var(--navy)">●</span> Lorem ipsum</div>
  <div class="tiny" style="left:122px;top:119px;width:55px">Lorem ipsum dolor sit amet, consectetuer adipiscing elit, sed diam nonummy nibh</div>
  <div class="label orange" style="left:190px;top:113px;font-size:4.5px"><span style="color:var(--navy)">●</span> Lorem ipsum</div>
  <div class="tiny" style="left:197px;top:119px;width:55px">Lorem ipsum dolor sit amet, consectetuer adipiscing elit, sed diam nonummy nibh</div>
</section>

<!-- Row 4 -->
<section class="slide" style="left:34px;top:525px">
  <div class="ph ph-sky" role="img" aria-label="Glass office building with palm trees" style="left:14px;top:20px;width:71px;height:115px"></div>
  <div class="sq-orange" style="left:75px;top:25px;width:17px;height:11px"></div>
  <div class="title" style="left:96px;top:25px;font-size:10px;font-weight:500">Lorem Ipsum Dolor Sit</div>
  <div class="sq-teal" style="left:256px;top:6px;width:10px;height:10px"></div>
  <div class="tiny" style="left:96px;top:40px;width:150px">Lorem ipsum dolor sit amet, consectetuer adipiscing elit, sed diam nonummy nibh euismod tincidunt erat volutpat. Ut wisi enim ad minim veniam, quis nostrud exerci tation ullamcorper suscipit<br><br>lobortis nisl ut aliquip ex ea commodo consequat. Ut wisi enim ad minim veniam, quis nostrud exerci tation ullamcorper suscipit lobortis nisl ut aliquip ex ea commodo consequat. Ut wisi enim ad minim veniam, quis nostrud exerci tation ullamcorper suscipit.</div>
  <div class="ph ph-city" role="img" aria-label="City skyline" style="left:96px;top:86px;width:68px;height:43px"></div>
  <div class="ph ph-house" role="img" aria-label="Modern gabled house" style="left:174px;top:86px;width:68px;height:43px"></div>
</section>

<section class="slide" style="left:317px;top:525px">
  <div class="sq-orange" style="left:10px;top:16px;width:9px;height:9px"></div>
  <div class="ph ph-city" role="img" aria-label="Aerial view of a dense city" style="left:13px;top:20px;width:72px;height:115px"></div>
  <div class="sq-teal" style="left:108px;top:0;width:124px;height:8px"></div>
  <div class="title" style="left:90px;top:26px;width:170px;text-align:center;font-size:11px;font-weight:500">Tation Ullamcorper</div>
  <div class="tiny" style="left:100px;top:42px;width:150px;text-align:center">Lorem ipsum dolor sit amet, consectetuer adipiscing elit, sed diam nonummy nibh euismod tincidunt erat volutpat. Ut wisi enim ad minim veniam, quis nostrud exerci tation ullamcorper suscipit<br><br>lobortis nisl ut aliquip ex ea commodo consequat. Ut wisi enim ad minim veniam, quis nostrud exerci tation suscipit lobortis nisl ut aliquip ex ea commodo consequat.</div>
  <div class="ph ph-house" role="img" aria-label="Blue house with dormer windows" style="left:96px;top:86px;width:149px;height:49px"></div>
</section>

<section class="slide" style="left:598px;top:525px">
  <div class="title" style="left:26px;top:15px;font-size:11px;font-weight:500">Text Added Here</div>
  <div class="sq-orange" style="left:42px;top:35px;width:50px;height:3px"></div>
  <div class="sq-teal" style="left:0;top:90px;width:57px;height:62px"></div>
  <div class="ph ph-house" role="img" aria-label="Stone cottage with lawn" style="left:22px;top:36px;width:90px;height:104px"></div>
  <div class="num-dot" style="left:125px;top:45px">1</div>
  <div class="tiny" style="left:145px;top:44px;width:100px">Lorem ipsum dolor sit amet, consectetuer adipiscing elit, sed diam nonummy nibh euismod tincidunt ut laoreet dolore magna aliquam erat volutpat. Ut wisi enim ad minim veniam</div>
  <div class="num-dot" style="left:125px;top:81px">2</div>
  <div class="tiny" style="left:145px;top:78px;width:100px">ullamcorper suscipit lobortis nisl ut aliquip ex ea commodo consequat. Duis autem vel eum iriure dolor in hendrerit<br><br>molestie consequat, vel illum dolore eu feugiat nulla facilisis at vero eros</div>
  <div class="num-dot" style="left:125px;top:115px">3</div>
  <div class="tiny" style="left:145px;top:113px;width:100px">Lorem ipsum dolor sit amet, consectetuer adipiscing elit, sed diam nonummy nibh euismod tincidunt ut laoreet dolore magna aliquam erat volutpat. Ut wisi enim ad minim veniam</div>
</section>

<!-- Row 5 -->
<section class="slide" style="left:34px;top:687px">
  <div class="sq-teal" style="left:16px;top:24px;width:10px;height:10px"></div>
  <div class="title" style="left:20px;top:40px;font-size:17px;font-weight:500">What's<br>A Domain?</div>
  <div class="tiny" style="left:20px;top:93px;width:85px">Lorem ipsum dolor sit amet, consectetuer adipiscing elit, sed diam nonummy nibh euismod tincidunt ut laoreet dolore<br><br>magna aliquam erat volutpat. Ut wisi enim ad minim veniam, quis nostrud exerci tation ullamcorper</div>
  <ul class="bullets" style="left:142px;top:48px">
    <li>Fits your business or products</li>
    <li>Is easy to spell and remember</li>
    <li>Fits your business or products</li>
    <li>Is easy to spell and remember</li>
    <li>Fits your business or products</li>
    <li>Is easy to spell and remember</li>
  </ul>
  <div class="sq-orange" style="left:138px;top:136px;width:10px;height:16px"></div>
</section>

<section class="slide" style="left:317px;top:687px">
  <div class="sq-teal" style="left:17px;top:14px;width:11px;height:11px"></div>
  <div class="title" style="left:35px;top:14px;font-size:11px;font-weight:500">Subtitle Text</div>
  <div class="ph ph-house" role="img" aria-label="Large white farmhouse estate" style="left:17px;top:37px;width:228px;height:67px"></div>
  <div class="abs" style="left:22px;top:96px;width:16px;height:12px;background:#fff;font-family:'Montserrat',sans-serif;font-weight:800;font-size:7px;color:var(--orange);text-align:center">01</div>
  <div class="abs" style="left:103px;top:96px;width:16px;height:12px;background:#fff;font-family:'Montserrat',sans-serif;font-weight:800;font-size:7px;color:var(--orange);text-align:center">02</div>
  <div class="abs" style="left:181px;top:96px;width:16px;height:12px;background:#fff;font-family:'Montserrat',sans-serif;font-weight:800;font-size:7px;color:var(--orange);text-align:center">03</div>
  <div class="tiny" style="left:43px;top:108px;width:50px">Lorem Ipsum Dolor sit amet Consectetur adipiscing<br><br>sed do eiusmod Tempor incididunt ut labore et dolore</div>
  <div class="tiny" style="left:122px;top:108px;width:50px">Lorem Ipsum Dolor sit amet Consectetur adipiscing<br><br>sed do eiusmod Tempor incididunt ut labore et dolore</div>
  <div class="tiny" style="left:200px;top:108px;width:50px">Lorem Ipsum Dolor sit amet Consectetur adipiscing<br><br>sed do eiusmod Tempor incididunt ut labore et dolore</div>
</section>

<section class="slide" style="left:598px;top:687px">
  <div class="sq-teal" style="left:9px;top:9px;width:9px;height:9px"></div>
  <div class="title" style="left:17px;top:22px;font-size:15px;font-weight:500">Our<br>Story</div>
  <div class="ph ph-people" role="img" aria-label="Two business people talking outside an office tower" style="left:111px;top:0;width:159px;height:78px"></div>
  <div class="sq-teal" style="left:0;top:78px;width:111px;height:61px"></div>
  <div class="tiny white" style="left:12px;top:87px;width:90px">Lorem ipsum dolor sit amet, consectetuer adipiscing elit, sed diam nonummy nibh euismod tincidunt ut laoreet dolore magna aliquam erat volutpat. Ut wisi enim ad minim veniam, quis nostrud exerci tation ullamcorper suscipit lobortis nisl ut aliquip ex ea commodo consequat. Duis autem vel eum iriure dolor in hendrerit in<br><br>Lorem ipsum dolor sit amet, consectetuer</div>
  <div class="tiny" style="left:125px;top:86px;width:62px">Lorem ipsum dolor sit amet, consectetuer adipiscing elit, sed diam nonummy nibh euismod tincidunt ut laoreet dolore magna aliquam erat ullamcorper suscipit lobortis nisl ut aliquip ex ea commodo consequat. Duis autem vel eum iriure dolor in hendrerit in<br><br>Lorem ipsum dolor sit amet, consectetuer adipiscing</div>
  <div class="tiny" style="left:193px;top:86px;width:62px">Lorem ipsum dolor sit amet, consectetuer adipiscing elit, sed diam ut aliquip ex ea commodo consequat. Duis autem vel eum iriure dolor in hendrerit in<br><br>Lorem ipsum dolor sit amet, consectetuer adipiscing elit, sed diam nonummy nibh euismod tincidunt ut laoreet ea commodo consequat. Duis autem</div>
</section>

<!-- Row 6 -->
<section class="slide" style="left:34px;top:851px">
  <div class="sq-teal" style="left:0;top:6px;width:21px;height:10px"></div>
  <div class="title" style="left:26px;top:6px;font-size:10px;font-weight:500">Company Timeline</div>
  <svg style="left:0;top:0" width="270" height="152" viewBox="0 0 270 152">
    <g fill="none" stroke="var(--orange)" stroke-width="1">
      <line x1="25" y1="64" x2="38" y2="64" stroke-dasharray="3 2"/>
      <path d="M38 64 H225 A20 21 0 0 1 225 106 H38"/>
      <line x1="25" y1="106" x2="38" y2="106" stroke-dasharray="3 2"/>
    </g>
    <g fill="#fff" stroke="var(--navy)" stroke-width=".8">
      <circle cx="54" cy="64" r="2"/><circle cx="84" cy="64" r="2"/><circle cx="114" cy="64" r="2"/><circle cx="144" cy="64" r="2"/><circle cx="174" cy="64" r="2"/><circle cx="204" cy="64" r="2"/>
      <circle cx="54" cy="106" r="2"/><circle cx="84" cy="106" r="2"/><circle cx="114" cy="106" r="2"/><circle cx="144" cy="106" r="2"/><circle cx="174" cy="106" r="2"/><circle cx="204" cy="106" r="2"/>
    </g>
    <g font-family="Roboto,sans-serif" font-weight="700" font-size="7" text-anchor="middle">
      <text x="54" y="74" fill="var(--orange)">Jan</text><text x="84" y="74" fill="var(--navy)">Feb</text><text x="114" y="74" fill="var(--orange)">Mar</text><text x="144" y="74" fill="var(--navy)">Apr</text><text x="174" y="74" fill="var(--orange)">May</text><text x="204" y="74" fill="var(--navy)">Jun</text>
      <text x="54" y="96" fill="var(--orange)">Dec</text><text x="84" y="96" fill="var(--navy)">Nov</text><text x="114" y="96" fill="var(--orange)">Oct</text><text x="144" y="96" fill="var(--navy)">Sep</text><text x="174" y="96" fill="var(--orange)">Aug</text><text x="204" y="96" fill="var(--navy)">Jul</text>
    </g>
    <g font-family="Roboto,sans-serif" font-size="6" fill="var(--navy)">
      <text x="42" y="38">01</text><text x="72" y="38">02</text><text x="102" y="38">03</text><text x="132" y="38">04</text><text x="162" y="38">05</text><text x="192" y="38">06</text>
      <text x="42" y="122">12</text><text x="72" y="122">11</text><text x="102" y="122">10</text><text x="132" y="122">09</text><text x="162" y="122">08</text><text x="192" y="122">07</text>
    </g>
  </svg>
  <div class="tiny" style="left:42px;top:40px;width:26px">Lorem ipsum dolor sit amet, adipiscing elit</div>
  <div class="tiny" style="left:72px;top:40px;width:26px">Lorem ipsum dolor sit amet, adipiscing elit</div>
  <div class="tiny" style="left:102px;top:40px;width:26px">Lorem ipsum dolor sit amet, adipiscing elit</div>
  <div class="tiny" style="left:132px;top:40px;width:26px">Lorem ipsum dolor sit amet, adipiscing elit</div>
  <div class="tiny" style="left:162px;top:40px;width:26px">Lorem ipsum dolor sit amet, adipiscing elit</div>
  <div class="tiny" style="left:192px;top:40px;width:26px">Lorem ipsum dolor sit amet, adipiscing elit</div>
  <div class="tiny" style="left:42px;top:124px;width:26px">Lorem ipsum dolor sit amet, adipiscing elit</div>
  <div class="tiny" style="left:72px;top:124px;width:26px">Lorem ipsum dolor sit amet, adipiscing elit</div>
  <div class="tiny" style="left:102px;top:124px;width:26px">Lorem ipsum dolor sit amet, adipiscing elit</div>
  <div class="tiny" style="left:132px;top:124px;width:26px">Lorem ipsum dolor sit amet, adipiscing elit</div>
  <div class="tiny" style="left:162px;top:124px;width:26px">Lorem ipsum dolor sit amet, adipiscing elit</div>
  <div class="tiny" style="left:192px;top:124px;width:26px">Lorem ipsum dolor sit amet, adipiscing elit</div>
</section>

<section class="slide" style="left:317px;top:851px">
  <div class="num-dot" style="left:19px;top:40px;width:20px;height:20px;font-size:10px">1</div>
  <div class="title" style="left:46px;top:40px;font-size:12px">Lorem<br>ipsum dolor<br>sit amet</div>
  <div class="tiny" style="left:46px;top:92px;width:75px;font-size:5px">Praesent bibendum at risus ac blandit. In eu risus vel felis elementum venenatis vitae sed lacus. Curabitur vel erat urna.</div>
  <div class="sq-teal" style="left:142px;top:33px;width:102px;height:90px"></div>
  <div class="num-dot" style="left:132px;top:40px;width:20px;height:20px;font-size:10px">2</div>
  <div class="title" style="left:159px;top:40px;font-size:12px;color:var(--navy)">Lorem<br>ipsum dolor<br>sit amet</div>
  <div class="tiny white" style="left:159px;top:90px;width:78px;font-size:5px">Praesent bibendum at risus ac blandit. In eu risus vel felis elementum venenatis vitae sed lacus. Curabitur vel erat urna.</div>
</section>

<section class="slide" style="left:598px;top:851px">
  <div class="sq-teal" style="left:9px;top:11px;width:9px;height:9px"></div>
  <div class="title" style="left:22px;top:11px;font-size:10px;font-weight:500">Company Costs</div>
  <svg style="left:0;top:0" width="270" height="152" viewBox="0 0 270 152">
    <rect x="21" y="70" width="125" height="5" fill="var(--orange)"/>
    <rect x="146" y="70" width="102" height="5" fill="var(--navy)"/>
    <path d="M248 67 L255 72.5 L248 78 Z" fill="var(--navy)"/>
    <g fill="none" stroke-width="3.5">
      <circle cx="65" cy="60" r="12" stroke="var(--orange)"/>
      <circle cx="112" cy="60" r="12" stroke="var(--navy)"/>
      <circle cx="159" cy="60" r="12" stroke="var(--orange)"/>
      <circle cx="207" cy="60" r="12" stroke="var(--navy)"/>
    </g>
    <g fill="var(--orange)"><circle cx="65" cy="60" r="7"/><circle cx="159" cy="60" r="7"/></g>
    <g fill="var(--navy)"><circle cx="112" cy="60" r="7"/><circle cx="207" cy="60" r="7"/></g>
    <g font-family="Roboto,sans-serif" font-size="3.5" fill="#fff" text-anchor="middle"><text x="75" y="74">Step 01</text><text x="122" y="74">Step 02</text><text x="169" y="74">Step 03</text><text x="225" y="74">Step 04</text></g>
    <g stroke="#999" stroke-width=".5"><line x1="65" y1="78" x2="65" y2="86"/><line x1="112" y1="78" x2="112" y2="86"/><line x1="159" y1="78" x2="159" y2="86"/><line x1="207" y1="78" x2="207" y2="86"/></g>
  </svg>
  <div class="label" style="left:45px;top:90px;width:40px;text-align:center">Lorem Ipsum</div>
  <div class="tiny" style="left:47px;top:97px;width:36px;text-align:center">Lorem ipsum dolor sit amet, consectetuer adipiscing elit sed diam nonummy nibh</div>
  <div class="label orange" style="left:92px;top:90px;width:40px;text-align:center">Lorem Ipsum</div>
  <div class="tiny" style="left:94px;top:97px;width:36px;text-align:center">Lorem ipsum dolor sit amet, consectetuer adipiscing elit sed diam nonummy nibh</div>
  <div class="label" style="left:139px;top:90px;width:40px;text-align:center">Lorem Ipsum</div>
  <div class="tiny" style="left:141px;top:97px;width:36px;text-align:center">Lorem ipsum dolor sit amet, consectetuer adipiscing elit sed diam nonummy nibh</div>
  <div class="label orange" style="left:187px;top:90px;width:40px;text-align:center">Lorem Ipsum</div>
  <div class="tiny" style="left:189px;top:97px;width:36px;text-align:center">Lorem ipsum dolor sit amet, consectetuer adipiscing elit sed diam nonummy nibh</div>
</section>

<!-- Row 7 -->
<section class="slide" style="left:34px;top:1013px">
  <div class="title" style="left:8px;top:14px;font-size:10px;font-weight:500">Text Here</div>
  <div class="tiny" style="left:8px;top:26px;width:80px">Lorem ipsum dolor sit amet, consectetuer adipiscing elit, sed diam nonummy nibh euismod tincidunt ut laoreet dolore magna aliquam erat volutpat. Ut wisi enim ad minim veniam,<br><br>quis nostrud exerci tation ullamcorper suscipit lobortis nisl ut aliquip ex ea commodo consequat. Duis autem vel eum iriure dolor in hendrerit in vulputate velit esse<br><br>Lorem ipsum dolor sit amet, consectetuer adipiscing elit, sed diam nonummy nibh euismod</div>
  <div class="sq-teal" style="left:0;top:81px;width:87px;height:53px"></div>
  <div class="abs" style="left:13px;top:86px;font-size:6px;font-weight:700;color:#fff">1.</div>
  <div class="label" style="left:24px;top:86px;font-size:3.5px">Lorem ipsum</div>
  <div class="tiny white" style="left:24px;top:90px;width:58px">Lorem ipsum dolor sit amet, consectetuer adipiscing elit, sed diam</div>
  <div class="abs" style="left:13px;top:102px;font-size:6px;font-weight:700;color:#fff">2.</div>
  <div class="label" style="left:24px;top:102px;font-size:3.5px">Lorem ipsum</div>
  <div class="tiny white" style="left:24px;top:106px;width:58px">Lorem ipsum dolor sit amet, consectetuer adipiscing elit, sed diam</div>
  <div class="abs" style="left:13px;top:118px;font-size:6px;font-weight:700;color:#fff">3.</div>
  <div class="label" style="left:24px;top:118px;font-size:3.5px">Lorem ipsum</div>
  <div class="tiny white" style="left:24px;top:122px;width:58px">Lorem ipsum dolor sit amet, consectetuer adipiscing elit, sed diam</div>
  <div class="phone" style="left:117px;top:17px;width:32px;height:68px"></div>
  <div class="abs" style="left:120px;top:30px;font-size:4px;color:var(--navy)">Lorem<br>ipsum dolor</div>
  <div class="tiny" style="left:120px;top:57px;width:26px">To introduce the students to the changing landscape of marketing</div>
  <div class="phone" style="left:158px;top:40px;width:32px;height:68px"></div>
  <div class="abs" style="left:161px;top:53px;font-size:4px;color:var(--navy)">Dolor sit<br>amet, conse</div>
  <div class="tiny" style="left:161px;top:80px;width:26px">You will learn concepts and ideas in digital marketing as well</div>
  <div class="phone" style="left:200px;top:63px;width:32px;height:68px"></div>
  <div class="abs" style="left:203px;top:76px;font-size:4px;color:var(--navy)">Consec</div>
  <div class="tiny" style="left:203px;top:103px;width:26px">You are required to pass 80% of the evaluation test</div>
</section>

<section class="slide" style="left:317px;top:1013px">
  <div class="sq-teal" style="left:14px;top:13px;width:9px;height:9px"></div>
  <div class="title" style="left:14px;top:26px;font-size:17px;font-weight:500">Our Team</div>
  <div class="sq-teal" style="left:0;top:77px;width:270px;height:51px"></div>
  <div class="avatar" style="left:26px;top:65px" role="img" aria-label="Team member portrait"></div>
  <div class="avatar" style="left:91px;top:65px" role="img" aria-label="Team member portrait"></div>
  <div class="avatar" style="left:155px;top:65px" role="img" aria-label="Team member portrait"></div>
  <div class="avatar" style="left:220px;top:65px" role="img" aria-label="Team member portrait"></div>
  <div class="label" style="left:16px;top:90px;width:40px;text-align:center;font-size:4.5px">ALEX REED</div>
  <div class="tiny white" style="left:18px;top:96px;width:36px;text-align:center">Ipsum dolor sit amet, cons ectetuer adipiscing elit, sed diam nonummy nibh euismod</div>
  <div class="label" style="left:81px;top:90px;width:40px;text-align:center;font-size:4.5px">NORA HALE</div>
  <div class="tiny white" style="left:83px;top:96px;width:36px;text-align:center">Ipsum dolor sit amet, cons ectetuer adipiscing elit, sed diam nonummy nibh euismod</div>
  <div class="label" style="left:145px;top:90px;width:40px;text-align:center;font-size:4.5px">ALEX REED</div>
  <div class="tiny white" style="left:147px;top:96px;width:36px;text-align:center">Ipsum dolor sit amet, cons ectetuer adipiscing elit, sed diam nonummy nibh euismod</div>
  <div class="label" style="left:210px;top:90px;width:40px;text-align:center;font-size:4.5px">NORA HALE</div>
  <div class="tiny white" style="left:212px;top:96px;width:36px;text-align:center">Ipsum dolor sit amet, cons ectetuer adipiscing elit, sed diam nonummy nibh euismod</div>
</section>

<section class="slide" style="left:598px;top:1013px">
  <div class="brand" style="left:12px;top:14px"><i></i>Quarry Lending</div>
  <div class="title" style="left:24px;top:55px;width:80px;text-align:right;font-size:24px">Thank<br>You</div>
  <div class="ph ph-modern" role="img" aria-label="Modern house with wood and stone facade" style="left:109px;top:44px;width:100px;height:72px"></div>
  <div class="url-strip" style="left:218px;top:44px;width:14px;height:72px"><span>quarrylending.com</span></div>
  <div class="sq-orange" style="left:8px;top:138px;width:7px;height:7px"></div>
</section>

</div>
</body>
</html>
```